Manufacturing Company Business card

K & T is a leading supplier of complex machine parts, assemblies and sub assemblies to the aerospace industry.
we would like to create a new feel for our manufacturing company business card design.
We are into lean manufacturing, bold design, metal, use current logo, use "this is your life" logo for entire back of card. updated look for 2015, text, bardcode, etc

our primary end use is flight control components used on about all commercial and business jets in use as well as military aircraft and civil aviation.
Updates

Reason: Need more time to review with internal team at KTmfg:)

Target Market(s)

aerospace, manufacturing

Industry/Entity Type

Aero

Contact Information for Business Card

New, industrial, trendy, use current logo, we like text, vmail is lame :( cell ph is ok - what is a fax???

Font styles to use
Serif
Sans Serif

Requirements
Must have
• incorporate our current logo, one option is an Industrial look, metal etc. we can also try to incorporate the feel of the back of the card onto the front but not so busy.
• Back of card full size "this is your life"
• front side, barcode, cell, - our motto "solutions in manufacturing" tm
Nice to have
• Professional look
• up to date
• appeals to broad audience
Should not have
• too much content - pictures of planes

```html
<!DOCTYPE html>
<html lang="en">
<head>
<meta charset="utf-8">
<title>K &amp; T Manufacturing – Business Card</title>
<link rel="stylesheet" href="https://fonts.googleapis.com/css2?family=Arimo:wght@700&family=Open+Sans:wght@400;600&display=swap">
<style>
  :root {
    --page-bg: #e9e7e3;
    --front-light: #f4f4f4;
    --front-mid: #dcdcdc;
    --front-dark: #c2c2c2;
    --texture-light: rgba(255,255,255,.55);
    --texture-fade: rgba(255,255,255,0);
    --ink: #2a2a2a;
    --rule: #9a9a9a;
    --back-top: #1c1c1c;
    --back-bottom: #050505;
    --accent-green: #1f5a34;
    --white: #ffffff;
  }
  * { margin: 0; padding: 0; box-sizing: border-box; }
  html, body { width: 1200px; height: 900px; overflow: hidden; }
  body {
    background: var(--page-bg);
    font-family: "Open Sans", Arial, sans-serif;
    position: relative;
  }
  .card {
    position: absolute;
    left: 300px;
    width: 600px;
    height: 343px;
    overflow: hidden;
    box-shadow: 0 10px 24px rgba(0,0,0,.25);
  }

  /* Front */
  .card-front {
    top: 60px;
    background: linear-gradient(100deg, var(--front-dark) 0%, var(--front-mid) 35%, var(--front-light) 70%, var(--front-mid) 100%);
    color: var(--ink);
  }
  .front-texture {
    position: absolute; left: 0; top: 60px; width: 330px; height: 230px;
    background: radial-gradient(ellipse at 25% 60%, var(--texture-light), var(--texture-fade) 70%);
  }
  .brand {
    position: absolute; left: 210px; top: 56px;
    display: flex; align-items: center; gap: 12px;
  }
  .brand-dot {
    width: 20px; height: 20px; border-radius: 50%;
    background: var(--ink);
  }
  .brand-name {
    font-weight: 600; font-size: 26px; letter-spacing: 2px; color: var(--ink);
  }
  .rule {
    position: absolute; left: 0; width: 100%; height: 0;
    border-top: 1px solid var(--rule);
  }
  .rule-upper { top: 146px; }
  .rule-upper-2 { top: 150px; }
  .rule-lower { top: 236px; }
  .rule-lower-2 { top: 240px; }
  .contact-right, .contact-left { list-style: none; }
  .contact-right li, .contact-left li { display: flex; align-items: center; gap: 14px; }
  .contact-right {
    position: absolute; right: 22px; top: 164px;
    font-size: 15px; line-height: 30px; font-weight: 600;
  }
  .contact-right li { justify-content: flex-end; }
  .contact-left {
    position: absolute; left: 30px; top: 254px;
    font-size: 16px; line-height: 34px; font-weight: 600;
  }
  .icon { width: 18px; height: 18px; flex: none; }

  /* Back */
  .card-back {
    top: 470px;
    background: linear-gradient(160deg, var(--back-top), var(--back-bottom));
  }
  .back-lines { position: absolute; inset: 0; }
  .motto {
    position: absolute; left: 0; right: 0; top: 132px;
    text-align: center;
    font-family: "Arimo", Arial, sans-serif; font-weight: 700;
    font-size: 54px; color: var(--white); letter-spacing: 1px;
  }
</style>
</head>
<body>
  <section class="card card-front">
    <div class="front-texture" role="img" aria-label="Soft halftone dot texture"></div>
    <div class="brand">
      <span class="brand-dot"></span>
      <span class="brand-name">K &amp; T MANUFACTURING</span>
    </div>
    <div class="rule rule-upper"></div>
    <div class="rule rule-upper-2"></div>
    <ul class="contact-right">
      <li>Stree t48 H#207 , Sydney
        <svg class="icon" viewBox="0 0 24 24"><path d="M12 2a7 7 0 0 0-7 7c0 5 7 13 7 13s7-8 7-13a7 7 0 0 0-7-7zm0 9.5A2.5 2.5 0 1 1 12 6.5a2.5 2.5 0 0 1 0 5z" fill="#2a2a2a"/></svg>
      </li>
      <li>hello@ktmail.com
        <svg class="icon" viewBox="0 0 24 24"><text x="12" y="19" text-anchor="middle" font-family="Arial, sans-serif" font-weight="700" font-size="20" fill="#2a2a2a">@</text></svg>
      </li>
    </ul>
    <div class="rule rule-lower"></div>
    <div class="rule rule-lower-2"></div>
    <ul class="contact-left">
      <li>
        <svg class="icon" viewBox="0 0 24 24"><path d="M3 8c0-2 2-3 9-3s9 1 9 3v2h-5V8H8v2H3z M6 12h12l2 8H4z" fill="#2a2a2a"/></svg>
        001-3486-2
      </li>
      <li>
        <svg class="icon" viewBox="0 0 24 24" fill="none" stroke="#2a2a2a" stroke-width="2"><circle cx="12" cy="12" r="9"/><ellipse cx="12" cy="12" rx="4" ry="9"/><path d="M3 12h18M5 7h14M5 17h14"/></svg>
        www.KTmanufacture.com
      </li>
    </ul>
  </section>

  <section class="card card-back">
    <svg class="back-lines" viewBox="0 0 600 343" preserveAspectRatio="none">
      <g stroke="#1f5a34" stroke-width="1.2" opacity=".9">
        <line x1="0" y1="150" x2="600" y2="112"/>
        <line x1="0" y1="160" x2="600" y2="122"/>
        <line x1="0" y1="212" x2="600" y2="174"/>
        <line x1="0" y1="222" x2="600" y2="184"/>
        <line x1="0" y1="232" x2="600" y2="194"/>
      </g>
    </svg>
    <h1 class="motto">This is Your Life</h1>
  </section>
</body>
</html>
```